Christmas Flyer for Suburban London Cocktail Bar & Party Venue

We need a flyer with details of our Christmas Party drinks packages for party bookings. Tin Lantern is a local cocktail bar with an emphasis on providing a modern hospitality environment with a sense of fun and whimsy. We pride ourselves on not being generic, providing a community atmosphere and don't take ourselves too seriously and our brand reflects that.

Christmas is one of the most popular times of year and we host parties for many people in our local area. The flyer is intended to summarise our promotional deals and will be distributed to local businesses as well as being available in the bar for customers.

An overview of our mood board that influences 'tone', as we await rebranding, can be seen at https://au.pinvaultex.com/derwickhaul/commercial-bar-fit-out-inspiration/

Target Market(s)

21-35 Urban Professionals

Industry/Entity Type

Hospitality

Colors

Designer to choose colors to be used in the design.

Requirements
Must have
• The 4 offers contained in the copy text. Can be adjusted for legibility as long as the offers remain substantively the same.
• The logo of the bar. The standard logo is the gold version however that can be recoloured if appropriate.
• The Address Tin Lantern - 47 Marrow Crescent - Balham, SE28 4QT - This need not be prominent.
Nice to have
• Our social media locations
• facebook /tinlanternbar
• Instagram /tinlanternbar
Should not have
• Should not contain photographs or exceptionally generic stock imagery.

```html
<!DOCTYPE html>
<html lang="en">
<head>
<meta charset="utf-8">
<title>Tin Lantern – Xmas Party Packages</title>
<link href="https://fonts.googleapis.com/css2?family=Oswald:wght@600&family=Open+Sans:ital,wght@0,700;1,700&family=Tilt+Neon&display=swap" rel="stylesheet">
<style>
  :root {
    --wall-top: #2b2321;
    --wall-bottom: #171312;
    --neon-pink: #ff5aa8;
    --neon-pink-glow: #ff1f86;
    --neon-blue: #52d6f5;
    --neon-blue-glow: #1fb2e8;
    --frame-white: #fff8f0;
    --heading-orange: #f7a823;
    --price-blue: #2fa8da;
    --rule-blue: #2fa8da;
    --body-white: #ffffff;
    --logo-gold: #b89a4e;
    --tree-tone: rgba(79,162,58,.22);
    --glass-tone: rgba(58,167,200,.22);
  }
  * { box-sizing: border-box; margin: 0; padding: 0; }
  html, body { width: 927px; height: 1200px; overflow: hidden; background: var(--wall-bottom); }
  .flyer {
    position: relative;
    width: 927px;
    height: 1200px;
    overflow: hidden;
    font-family: "Open Sans", Arial, sans-serif;
    color: var(--body-white);
  }
  .brick-wall {
    position: absolute; inset: 0;
    background: radial-gradient(ellipse at 50% 40%, var(--wall-top) 0%, var(--wall-bottom) 85%);
  }
  .neon-sign {
    position: absolute;
    left: 210px; top: 27px; width: 493px; height: 243px;
    border: 4px solid var(--frame-white);
    border-radius: 16px;
    box-shadow: 0 0 10px rgba(255,255,255,.75), inset 0 0 10px rgba(255,255,255,.45);
    text-align: center;
    font-family: "Tilt Neon", "Trebuchet MS", sans-serif;
  }
  .neon-sign .line-xmas {
    position: absolute; left: 0; right: 0; top: 14px;
    font-size: 94px; letter-spacing: 26px; padding-left: 26px;
    color: #ffd0e6;
    -webkit-text-stroke: 2px var(--neon-pink);
    text-shadow: 0 0 6px var(--neon-pink-glow), 0 0 16px var(--neon-pink-glow);
  }
  .neon-sign .line-party {
    position: absolute; left: 0; right: 0; top: 118px;
    font-size: 88px; letter-spacing: 20px; padding-left: 20px;
    color: #cdf6ff;
    -webkit-text-stroke: 2px var(--neon-blue);
    text-shadow: 0 0 6px var(--neon-blue-glow), 0 0 16px var(--neon-blue-glow);
  }
  .neon-art, .drinks-icons { position: absolute; border-radius: 10px; }
  .neon-tree {
    left: 63px; top: 48px; width: 118px; height: 214px;
    background: linear-gradient(180deg, var(--tree-tone), rgba(79,162,58,.08));
  }
  .neon-cocktail {
    left: 714px; top: 85px; width: 166px; height: 166px;
    background: linear-gradient(135deg, rgba(240,160,40,.2), var(--glass-tone) 45%, rgba(58,167,200,.08));
  }
  .drinks-icons {
    width: 168px; height: 104px;
    background: linear-gradient(90deg, rgba(214,196,60,.22), rgba(110,180,60,.22), rgba(220,40,120,.22));
  }
  .offer { position: absolute; }
  .offer-title {
    font-family: "Oswald", "Arial Narrow", sans-serif;
    font-weight: 600;
    font-size: 27px;
    line-height: 1;
    letter-spacing: .4px;
    text-transform: uppercase;
    color: var(--heading-orange);
    padding-bottom: 10px;
    border-bottom: 2px solid var(--rule-blue);
  }
  .offer-price {
    font-style: italic;
    font-weight: 700;
    font-size: 24px;
    color: var(--price-blue);
    margin: 12px 0 0 10px;
  }
  .offer-items {
    list-style: none;
    font-weight: 700;
    font-size: 22px;
    line-height: 35px;
    white-space: nowrap;
  }
  .offer-items .indent { padding-left: 27px; }

  .sharing-combo .offer-title,
  .package-3 .offer-title { padding-left: 8px; }

  .sharing-combo { left: 49px; top: 364px; width: 267px; }
  .sharing-combo .offer-items { margin: 18px 0 0 8px; }

  .package-1 { left: 442px; top: 366px; width: 403px; }
  .package-1 .offer-price { margin-left: 21px; }
  .package-1 .offer-items { margin: 16px 0 0 33px; }

  .package-2 { left: 49px; top: 650px; width: 398px; }
  .package-2 .offer-price { margin-left: 13px; }
  .package-2 .offer-items { margin: 52px 0 0 4px; }

  .package-3 { left: 442px; top: 766px; width: 416px; }
  .package-3 .offer-price { margin-left: 19px; }
  .package-3 .offer-items { margin: 40px 0 0 21px; }

  .brand-block {
    position: absolute;
    left: 60px; top: 1000px; width: 330px;
    color: var(--logo-gold);
  }
  .brand-name {
    display: flex; align-items: center; gap: 12px;
    font-weight: 700;
    font-size: 46px;
    line-height: 1;
  }
  .brand-name .mark {
    width: 22px; height: 22px; border-radius: 50%;
    background: var(--logo-gold);
    flex: none;
  }
  .venue-address {
    margin-top: 16px;
    font-weight: 700;
    font-size: 15px;
    line-height: 22px;
    letter-spacing: .3px;
  }
</style>
</head>
<body>
<main class="flyer">
  <div class="brick-wall" role="img" aria-label="Dark red brick wall background"></div>

  <div class="neon-art neon-tree" role="img" aria-label="Green neon Christmas tree"></div>
  <div class="neon-art neon-cocktail" role="img" aria-label="Blue neon cocktail glass with orange slice and straw"></div>

  <header class="neon-sign">
    <div class="line-xmas">XMAS</div>
    <div class="line-party">PARTY</div>
  </header>

  <section class="offer sharing-combo">
    <h2 class="offer-title">Sharing Combo</h2>
    <p class="offer-price">£85 – Save up to £35</p>
    <ul class="offer-items">
      <li>3 of our sharing cocktails</li>
      <li>Bottle of Prosecco</li>
    </ul>
  </section>

  <section class="offer package-1">
    <h2 class="offer-title">Xmas Package 1 - 10 People</h2>
    <p class="offer-price">£150 - Save up to £65</p>
    <ul class="offer-items">
      <li>10x Cocktails</li>
      <li>10x Beers</li>
      <li>10x house spirit + mixer,</li>
      <li>glass of wine or prosecco</li>
      <li>Bottle of prosecco</li>
    </ul>
  </section>
  <div class="drinks-icons" style="left:712px; top:424px;" role="img" aria-label="Neon beer mug, bottle and cocktail glass icons"></div>

  <section class="offer package-2">
    <h2 class="offer-title">Xmas Package 2 - 15 People</h2>
    <p class="offer-price">£220 - Save up to £85</p>
    <ul class="offer-items">
      <li>+ 15x Cocktails</li>
      <li>+ 15x Beers</li>
      <li>+ 15x house spirit + mixer,</li>
      <li class="indent">glass of wine or prosecco</li>
      <li>+&nbsp; Sharing cocktail</li>
    </ul>
  </section>
  <div class="drinks-icons" style="left:249px; top:740px;" role="img" aria-label="Neon beer mug, bottle and cocktail glass icons"></div>

  <section class="offer package-3">
    <h2 class="offer-title">Xmas Package 3 - 20 People</h2>
    <p class="offer-price">£350 - Save up to £150</p>
    <ul class="offer-items">
      <li>+ 20x Cocktails</li>
      <li>+ 20x Beers</li>
      <li>+ 20x house spirit + mixer,</li>
      <li class="indent">glass of wine or prosecco</li>
      <li>+ Bottle of prosecco</li>
      <li>+ Treasure chest!</li>
      <li class="indent">(12 Person Sharer valued at £100)</li>
    </ul>
  </section>
  <div class="drinks-icons" style="left:714px; top:852px;" role="img" aria-label="Neon beer mug, bottle and cocktail glass icons"></div>

  <footer class="brand-block">
    <div class="brand-name"><span class="mark"></span>Tin Lantern</div>
    <p class="venue-address">47 Marrow Crescent · Balham, SE28 4QT</p>
  </footer>
</main>
</body>
</html>
```